Epoxy Flooring Contractor business card

We need a business card to promote a new addition to our business. We now offer Epoxy Flooring. We would like for the business card to include the images attached. One is our logo, the other is a sample of metallic epoxy flooring, we would like to incorporate that somewhere into the design. I was thinking an icon of a man pushing a concrete grinder and have the color set to the metallic epoxy color. I found a business card sample on this website, I will attach it. It has the icon that we are looking for, or something similar.
Our company name is Brightmore Coatings LLC
Our owners name is Dana Pellow
Phone is 561-847-2916
website is www.brightmore-coatingsllc.com
please let me know if you need any other info

Contact Information for Business Card

Brightmore Coatings LLC
Dana Pellow, owner
Phone: 561-847-2916
Address: P.O Box 8146 Lake Worth, FL 33471
www.Brightmore-CoatingsLLC.com
BrightmoreCoatingsLLC@mailvista.net
Include logo attached
It must include a Clip art of man with concrete grinder
Must include metallic epoxy design attached
Must include the following text
Residential Garage Flooring
Epoxy Countertops
Commercial Epoxy Flooring
Restaurant Flooring
Warehouse Flooring
Licensed & Insured
Free Estimates

Colors

Designer to choose colors to be used in the design.

Requirements
Must have
• Include logo attached
• It must include a Clip art of man with concrete grinder
• Must include metallic epoxy design attached
• Must include the following text
• Garage Epoxy Flooring
• Residential Epoxy Flooring
• Concrete Floor Crack Repairs
• Concrete Floor Grinding
• Commercial & Warehouse Epoxy Flooring
• Restaurant Epoxy Flooring
• Epoxy Countertops
• Non Slip Epoxy Pool Decks
• Textured Finishes, Flakes, Granite Coat, Metallic & Quartz
• FREE ESTIMATES • LICENSED & INSURED

```html
<!DOCTYPE html>
<html lang="en">
<head>
<meta charset="utf-8">
<title>Brightmore Coatings – Business Card</title>
<link rel="stylesheet" href="https://fonts.googleapis.com/css2?family=Montserrat:wght@500;700;800&family=Open+Sans:wght@400;600&display=swap">
<style>
  :root {
    --bg: #2b2c2f;
    --paper: #ffffff;
    --band: #4a6f98;
    --band-dark: #3e5f86;
    --accent-light: #7aa3cf;
    --logo-grey: #6a6a6a;
    --ink: #1e1e1e;
    --name-blue: #3f6390;
    --flake-a: #c9ced6;
    --flake-b: #3a3d44;
    --metal-a: #8fa8b8;
    --metal-b: #5d6a6c;
  }
  * { box-sizing: border-box; margin: 0; padding: 0; }
  html, body { width: 1200px; height: 1200px; overflow: hidden; }
  body { background: var(--bg); position: relative; font-family: "Open Sans", sans-serif; }

  .card {
    position: absolute; left: 160px; width: 880px; height: 503px;
    background: var(--paper); overflow: hidden;
    box-shadow: 0 12px 30px rgba(0,0,0,.45);
  }
  .card--front { top: 70px; }
  .card--back { top: 627px; }

  /* brand lockup */
  .brand { position: absolute; display: flex; align-items: center; gap: 14px; }
  .brand__square { width: 46px; height: 46px; background: var(--band); flex: none; }
  .brand__name {
    font-family: "Montserrat", sans-serif; font-weight: 500; color: var(--logo-grey);
    letter-spacing: 3px; line-height: 1.02;
  }
  .card--front .brand { left: 260px; top: 58px; }
  .card--front .brand__name { font-size: 40px; }

  /* services band */
  .services {
    position: absolute; left: 0; right: 0; top: 200px; height: 200px;
    background: var(--band);
    border-top: 6px solid var(--accent-light);
  }
  .services__label {
    position: absolute; left: 300px; top: 24px;
    background: var(--paper); color: var(--band);
    font-family: "Montserrat", sans-serif; font-weight: 700; font-size: 20px;
    padding: 6px 18px; letter-spacing: .5px;
  }
  .services__list {
    position: absolute; left: 40px; right: 40px; top: 86px;
    color: var(--paper); font-family: "Montserrat", sans-serif; font-weight: 700;
    font-size: 19px; line-height: 1.5; text-align: center;
  }

  .finish-samples { position: absolute; left: 0; right: 0; top: 400px; bottom: 0; display: flex; }
  .finish-samples__flake {
    flex: 1; background: linear-gradient(135deg, var(--flake-a), #9da3ad 45%, var(--flake-b) 70%, var(--flake-a));
  }
  .finish-samples__metallic {
    flex: 1; background: linear-gradient(120deg, var(--metal-a), var(--metal-b) 50%, #3b6ea8 75%, var(--metal-a));
  }

  /* back side */
  .card--back .brand { left: 120px; top: 205px; }
  .card--back .brand__name { font-size: 34px; }
  .divider { position: absolute; left: 475px; top: 140px; width: 2px; height: 215px; background: var(--band); }

  .contact { position: absolute; left: 510px; top: 140px; color: var(--ink); }
  .contact__name {
    font-family: "Montserrat", sans-serif; font-weight: 800; font-size: 30px;
    color: var(--name-blue); letter-spacing: .5px; line-height: 1;
  }
  .contact__role { font-size: 17px; margin-top: 4px; }
  .contact__company { font-size: 16px; color: var(--name-blue); margin-top: 10px; }
  .contact__address { font-size: 16px; }
  .contact__lines { list-style: none; margin-top: 14px; font-size: 15px; }
  .contact__lines li { display: flex; align-items: center; gap: 10px; height: 24px; }
  .contact__lines svg { width: 15px; height: 15px; fill: var(--band); flex: none; }

  .stripe { position: absolute; }
  .stripe--light { left: 0; bottom: 0; width: 560px; height: 12px; background: var(--accent-light); }
  .stripe--dark { left: 568px; right: 0; bottom: 0; height: 24px; background: var(--band-dark); }
</style>
</head>
<body>

<section class="card card--front" aria-label="Card front">
  <div class="brand">
    <span class="brand__square"></span>
    <div class="brand__name">Brightmore<br>Coatings</div>
  </div>

  <div class="services">
    <div class="services__label">OUR SERVICES</div>
    <p class="services__list">
      Residential Garage Flooring, Epoxy Countertops, Commercial Epoxy Flooring<br>
      Restaurant Flooring, Warehouse Flooring, Licensed &amp; Insured, Free Estimates
    </p>
  </div>

  <div class="finish-samples">
    <div class="finish-samples__flake" role="img" aria-label="Close-up of grey, black and blue flake epoxy floor"></div>
    <div class="finish-samples__metallic" role="img" aria-label="Metallic epoxy floor sample in silver and blue swirls"></div>
  </div>
</section>

<section class="card card--back" aria-label="Card back">
  <div class="brand">
    <span class="brand__square"></span>
    <div class="brand__name">Brightmore<br>Coatings</div>
  </div>

  <div class="divider"></div>

  <div class="contact">
    <h1 class="contact__name">DANA PELLOW</h1>
    <p class="contact__role">owner</p>
    <p class="contact__company">Brightmore Coatings LLC</p>
    <p class="contact__address">P.O Box 8146 Lake Worth, FL 33471</p>
    <ul class="contact__lines">
      <li>
        <svg viewBox="0 0 24 24"><path d="M6.6 10.8a15.1 15.1 0 0 0 6.6 6.6l2.2-2.2a1 1 0 0 1 1-.25 11.4 11.4 0 0 0 3.6.57 1 1 0 0 1 1 1V20a1 1 0 0 1-1 1A17 17 0 0 1 3 4a1 1 0 0 1 1-1h3.5a1 1 0 0 1 1 1c0 1.25.2 2.45.57 3.57a1 1 0 0 1-.25 1z"/></svg>
        +561 - 847 - 2916
      </li>
      <li>
        <svg viewBox="0 0 24 24"><path d="M2 5h20v14H2z M2 5l10 8 10-8" /></svg>
        BrightmoreCoatingsLLC@mailvista.net
      </li>
      <li>
        <svg viewBox="0 0 24 24"><path d="M12 2a10 10 0 1 0 0 20 10 10 0 0 0 0-20zm0 2c1 1.3 1.8 3.4 2 6h-4c.2-2.6 1-4.7 2-6zm-2 8h4c-.2 2.6-1 4.7-2 6-1-1.3-1.8-3.4-2-6zM4.1 11h3.9c.1-2 .5-3.9 1.3-5.4A8 8 0 0 0 4.1 11zm0 2a8 8 0 0 0 5.2 5.4c-.8-1.5-1.2-3.4-1.3-5.4zm15.8 0h-3.9c-.1 2-.5 3.9-1.3 5.4a8 8 0 0 0 5.2-5.4zm0-2a8 8 0 0 0-5.2-5.4c.8 1.5 1.2 3.4 1.3 5.4z"/></svg>
        www.Brightmore-CoatingsLLC.com
      </li>
    </ul>
  </div>

  <div class="stripe stripe--light"></div>
  <div class="stripe stripe--dark"></div>
</section>

</body>
</html>
```